Twin Ravens Sparkling

Hi all,

Thanks for taking the time to check out our brief.

Twin Ravens is an Australian wine company based in Victoria, and have been around for more than 20 years. We have a well-known sparkling Chardonnay Pinot Noir that needs a package revamp and we need your help!

Check out our current package here: http://www.twinravens.example.au/our-wines/dsp-default_b.cfm?loadref=17

So here's the brief:

1. Use of the Twin Ravens logo (silhouette) and text mandatory - but can be as small/large as required.

2. Design must be shown on a sparkling bottle.

3. Can be closed with cork or crown seal - neck label/hood not mandatory.

4. Front label size to be no larger than 75mm high x 100mm wide. Back label to be no larger than 75mm x 100mm

5. Label does not have to be square/rectangular. Happy to see thoughts outside the box.

6. Design cannot be printed onto the bottle - must be on a label that can be applied to the bottle.

7. Be forward thinking. Be interesting. This design does not have to tie into our still (red and white) wine range.

8. Mandatory information to be shown on front label - a. Wine of Australia - b. Sparkling Chardonnay Pinot Noir

9. Mandatory info for front label - a. 750mL - b. Alcohol e.g. 13.5% ALC/VOL - c. Wine of Australi - d. Producer address (please insert dummy address at this stage - e. standard drinks e.g. approx 8.0 standard drinks (this can also be shown in the standard drinks glass logo) - f. space for a tasting blurb

10. Try to stay away from anything floral or overly girly.

Requirements
Must have
• Design must be shown on a sparkling wine bottle & include the full label design separately
Should not have
• Try to stay away from anything too floral and overly girly.

```html
<!DOCTYPE html>
<html lang="en">
<head>
<meta charset="utf-8">
<title>Twin Ravens Sparkling – Label Design</title>
<link rel="stylesheet" href="https://fonts.googleapis.com/css2?family=Cinzel:wght@400;600&display=swap">
<style>
  :root {
    --paper: #ffffff;
    --stage: #000000;
    --foil: #ff9a98;
    --foil-deep: #e27d7b;
    --ink: #000000;
    --label-light: #e88a80;
    --label-dark: #6e2626;
    --label-edge: #f7c2b6;
    --label-text: #f6cdbf;
    --bottle-light: #8a3a36;
    --bottle-dark: #2a0d0c;
  }
  html, body {
    margin: 0;
    padding: 0;
    overflow: hidden;
    background: var(--paper);
  }
  .board {
    width: 1200px;
    height: 900px;
    position: relative;
    overflow: hidden;
    background: var(--paper);
  }
  .board svg { display: block; }
  .label-type {
    font-family: "Cinzel", "Times New Roman", serif;
    fill: var(--label-text);
  }
  .neck-name {
    font-family: "Cinzel", "Times New Roman", serif;
    fill: var(--ink);
  }
</style>
</head>
<body>
<main class="board">
  <svg width="1200" height="900" viewBox="0 0 1200 900" xmlns="http://www.w3.org/2000/svg">
    <defs>
      <linearGradient id="bottle-glass" x1="0" x2="1" y1="0" y2="0">
        <stop offset="0" stop-color="var(--bottle-dark)"/>
        <stop offset="0.3" stop-color="var(--bottle-light)"/>
        <stop offset="0.6" stop-color="#5a1f1c"/>
        <stop offset="1" stop-color="var(--bottle-dark)"/>
      </linearGradient>
      <radialGradient id="label-face" cx="0.5" cy="0.45" r="0.6">
        <stop offset="0" stop-color="var(--label-light)"/>
        <stop offset="1" stop-color="var(--label-dark)"/>
      </radialGradient>
    </defs>

    <!-- presentation stage -->
    <rect class="stage" x="382" y="0" width="818" height="900" fill="var(--stage)"/>

    <!-- bottle mock-up -->
    <g class="bottle-mockup" role="img" aria-label="Sparkling wine bottle wearing the pink neck foil and the Twin Ravens front label">
      <path class="bottle-glass" d="M150,20 L230,20 L230,150 Q234,300 290,420 Q302,450 302,500 L302,875 Q302,892 285,892 L95,892 Q78,892 78,875 L78,500 Q78,450 90,420 Q146,300 150,150 Z" fill="url(#bottle-glass)"/>
      <path class="bottle-foil" d="M146,8 Q190,0 234,8 L236,250 Q238,320 260,385 L130,385 Q142,320 144,250 Z" fill="var(--foil)"/>
      <path class="bottle-chevrons" d="M142,290 L190,320 L238,290 M146,312 L190,340 L234,312 M150,334 L190,360 L230,334" stroke="var(--ink)" stroke-width="9" fill="none"/>
      <path class="bottle-label" d="M120,625 Q120,605 150,605 L230,605 Q260,605 260,625 Q292,635 292,680 Q292,720 262,735 Q250,780 190,785 Q130,780 118,735 Q88,720 88,680 Q88,635 120,625 Z" fill="url(#label-face)" stroke="var(--label-edge)" stroke-width="2"/>
    </g>

    <!-- neck label, flat -->
    <g class="neck-label">
      <path class="neck-label-shape" d="M545,0 H1035 V380 Q985,415 913,405 Q840,395 790,345 Q740,395 668,405 Q596,415 545,380 Z" fill="var(--foil)"/>
      <polyline class="neck-band" points="545,248 760,248 790,228 820,248 1035,248" fill="none" stroke="var(--ink)" stroke-width="14" stroke-linejoin="miter"/>
      <g class="neck-chevrons" fill="none" stroke="var(--ink)" stroke-width="16" stroke-linejoin="miter">
        <polyline points="570,285 668,335 766,285"/>
        <polyline points="585,315 668,360 751,315"/>
        <polyline points="602,345 668,385 734,345"/>
        <polyline points="815,285 913,335 1011,285"/>
        <polyline points="830,315 913,360 996,315"/>
        <polyline points="847,345 913,385 979,345"/>
      </g>
      <g class="neck-mark">
        <rect class="neck-scroll" x="570" y="218" width="62" height="22" fill="var(--foil-deep)" role="img" aria-label="Curled flourish ornament"/>
        <rect class="neck-scroll" x="704" y="218" width="62" height="22" fill="var(--foil-deep)" role="img" aria-label="Curled flourish ornament"/>
        <circle cx="668" cy="212" r="30" fill="none" stroke="var(--foil-deep)" stroke-width="3"/>
        <text class="neck-name" x="668" y="266" font-size="13" letter-spacing="4" text-anchor="middle">TWIN RAVENS</text>
      </g>
      <g class="neck-mark">
        <rect class="neck-scroll" x="815" y="218" width="62" height="22" fill="var(--foil-deep)" role="img" aria-label="Curled flourish ornament"/>
        <rect class="neck-scroll" x="949" y="218" width="62" height="22" fill="var(--foil-deep)" role="img" aria-label="Curled flourish ornament"/>
        <circle cx="913" cy="212" r="30" fill="none" stroke="var(--foil-deep)" stroke-width="3"/>
        <text class="neck-name" x="913" y="266" font-size="13" letter-spacing="4" text-anchor="middle">TWIN RAVENS</text>
      </g>
    </g>

    <!-- front label, flat -->
    <g class="front-label">
      <path class="front-label-frame" d="M625,525 Q625,498 655,498 L885,498 Q915,498 915,525 Q1040,540 1040,660 Q1040,730 985,760 Q975,840 900,860 Q840,880 790,880 Q740,880 680,860 Q605,840 595,760 Q540,730 540,660 Q540,540 625,525 Z" fill="url(#label-face)" stroke="var(--label-edge)" stroke-width="4"/>
      <path class="front-label-inner" d="M640,540 Q640,516 665,516 L875,516 Q900,516 900,540 Q1020,555 1020,660 Q1020,720 968,748 Q960,825 895,842 Q840,860 790,860 Q740,860 685,842 Q620,825 612,748 Q560,720 560,660 Q560,555 640,540 Z" fill="none" stroke="var(--label-edge)" stroke-width="2" opacity="0.7"/>
      <g class="front-stars" fill="#ffffff">
        <polygon points="752,527 755,535 763,535 757,540 759,548 752,543 745,548 747,540 741,535 749,535"/>
        <polygon points="776,521 779,529 787,529 781,534 783,542 776,537 769,542 771,534 765,529 773,529"/>
        <polygon points="804,521 807,529 815,529 809,534 811,542 804,537 797,542 799,534 793,529 801,529"/>
        <polygon points="828,527 831,535 839,535 833,540 835,548 828,543 821,548 823,540 817,535 825,535"/>
      </g>
      <rect class="front-scroll" x="610" y="620" width="100" height="45" fill="#c8625c" role="img" aria-label="Curled flourish ornament"/>
      <rect class="front-scroll" x="870" y="620" width="100" height="45" fill="#c8625c" role="img" aria-label="Curled flourish ornament"/>
      <line class="front-rule" x1="575" y1="675" x2="1005" y2="675" stroke="var(--label-edge)" stroke-width="2"/>
      <circle class="front-seal" cx="790" cy="625" r="70" fill="#c25e58" stroke="var(--label-edge)" stroke-width="3"/>
      <text class="label-type" x="790" y="728" font-size="30" font-weight="600" letter-spacing="7" text-anchor="middle">TWIN RAVENS</text>
      <text class="label-type" x="790" y="760" font-size="17" text-anchor="middle">SPARKLING CHARDONNAY</text>
      <text class="label-type" x="790" y="782" font-size="17" text-anchor="middle">PINOT NOIR</text>
      <text class="label-type" x="790" y="803" font-size="9" text-anchor="middle">TASTING BLURB</text>
      <text class="label-type" x="790" y="826" font-size="15" text-anchor="middle">WINE OF AUSTRALIA</text>
      <text class="label-type" x="790" y="838" font-size="6" text-anchor="middle">13.5% ALC/VOL</text>
      <text class="label-type" x="790" y="847" font-size="5" text-anchor="middle">750ML</text>
    </g>
  </svg>
</main>
</body>
</html>
```